New Business Card Design Project

Looking for a modern business card design for an import distribution business for industrial technical products. The winning design will translate modern, sophistication, technical, professional and sustainable.

Target Market(s)

Technical customers

Industry/Entity Type

Business

Contact Information for Business Card

Dean Harlow
Sales Manager
M: 0471 625 183
P: 1300 872 619
dean@volkarsystems.com.au
4/18 Galloway Crest Road
Kenmore Park NSW 2163
www.volkarsystems.com.au

Font styles to use
Sans Serif

Colors
ec1f27
606060
000000
fbfbfb

Requirements
Must have
• My Logo which is the Volkar Systems logo attached
Nice to have
• Eurostile Bold font

```html
<!DOCTYPE html>
<html lang="en">
<head>
<meta charset="utf-8">
<title>Volkar Systems – Business Card</title>
<link rel="stylesheet" href="https://fonts.googleapis.com/css2?family=Arimo:wght@400;700&display=swap">
<style>
  :root {
    --red: #e61b0f;
    --card-black: #0a0a0b;
    --white: #ffffff;
    --page: #fefefe;
    --edge: #f1d6d3;
  }
  * { margin: 0; padding: 0; box-sizing: border-box; }
  html, body { width: 1200px; height: 1000px; overflow: hidden; background: var(--page); }
  body { position: relative; font-family: "Arimo", Arial, sans-serif; }

  .card {
    position: absolute;
    left: 346px;
    width: 508px;
    height: 328px;
    background: var(--card-black);
    outline: 1px solid var(--edge);
    overflow: hidden;
  }
  .card--front { top: 158px; }
  .card--back { top: 514px; height: 327px; }

  .brand {
    position: absolute;
    display: flex;
    align-items: center;
    gap: 14px;
    left: 0; right: 0;
    justify-content: center;
  }
  .card--front .brand { top: 92px; }
  .card--back .brand { top: 137px; }
  .brand__square { width: 40px; height: 40px; background: var(--red); }
  .brand__name {
    font-weight: 700;
    font-size: 29px;
    letter-spacing: 1px;
    color: var(--red);
    text-transform: uppercase;
  }

  .panels { position: absolute; left: 0; top: 182px; }

  .contact {
    position: absolute;
    color: var(--white);
    font-size: 12.5px;
    line-height: 16px;
    white-space: nowrap;
  }
  .contact--person { left: 15px; top: 212px; }
  .contact--office { left: 290px; top: 245px; }
  .contact__name { font-weight: 700; font-size: 15px; line-height: 18px; }
</style>
</head>
<body>
  <section class="card card--front">
    <div class="brand">
      <span class="brand__square"></span>
      <span class="brand__name">Volkar Systems</span>
    </div>

    <svg class="panels" width="508" height="146" viewBox="0 0 508 146" aria-hidden="true">
      <path d="M0 0 H191 A42 42 0 0 1 233 42 V146 H0 Z" fill="var(--red)"/>
      <path d="M320 0 H508 V146 H278 V42 A42 42 0 0 1 320 0 Z" fill="var(--red)"/>
    </svg>

    <div class="contact contact--person">
      <p class="contact__name">Dean Harlow</p>
      <p>Sales Manager</p>
      <p>M: 0471 625 183</p>
      <p>P: 1300 872 619</p>
      <p>dean@volkarsystems.com.au</p>
    </div>

    <div class="contact contact--office">
      <p>4/18 Galloway Crest Road</p>
      <p>Kenmore Park NSW 2163</p>
      <p>www.volkarsystems.com.au</p>
    </div>
  </section>

  <section class="card card--back">
    <div class="brand">
      <span class="brand__square"></span>
      <span class="brand__name">Volkar Systems</span>
    </div>
  </section>
</body>
</html>
```